Luxury Wine Label for New Startup Winery

We need a wine label for our new winery startup. We have worked with a local designer but do not feel the resulting label / logo have the elevation required to present our brand as a luxury wine. Our winery is called "Harrowgate Vineyards" and we are focused on extremely high quality hand crafted artisan and estate wines from the Pacific Northwest.
We would like to see designs that utilize a tree line, or other imagery that represents the "Harrowgate" part of our company name. Another interesting feature could be wood grain.
A logo will be required based on your design so please design with this in mind:
This logo should be consistent with the wine bottle label design, and should be representative of our high end exclusive wine while giving a sense of place (Oregon/ Pacific Northwest.)
I will supply an image of the design we received from our local designer, PLEASE NOTE: in general we do like wood grain and tree line concepts but feel the execution was poorly done.
ATTN: Logo design should be suitable for use on: Bottles (Red wine/rose/white wine), Bussiness cards, vehicle signage, business signage, etc
P.S.:
If you have a design that is not outside the box we are still interested in seeing it.
Label is for a burgundy style bottle with a label height of 3.5 - 4" and a width of 3.5-4"
any label <= 4"x4" and >=3.5"x3.5" will be acceptable:
HOWEVER Width should be greater than or equal to height due to the bottle format
Target Market(s)
Wine enthusiasts with adequate discretionary budgets to afford $100 bottles of wine.
Industry/Entity Type
Wine / Winery
Requirements
Must have
- A sense of luxury, a feel of exclusivity, and a theme consistent with our product and brand name
Nice to have
- Tree line, wood grain or other wood themes. Serif fonts
Should not have
- anything cheesy, off topic, hard to read script fonts or anything that makes the label hard to read from a few feet away or too busy

```html
<!DOCTYPE html>
<html lang="en">
<head>
<meta charset="utf-8">
<title>Harrowgate Vineyards — Syrah Label</title>
<link href="https://fonts.googleapis.com/css2?family=Cinzel:wght@400;500&family=Cormorant+Garamond:wght@500;600&display=swap" rel="stylesheet">
<style>
  :root {
    --backdrop: #2c2c2d;
    --label-black: #141415;
    --label-black-soft: #1c1c1e;
    --forest-high: #4a4a50;
    --forest-mid: #2a2a2e;
    --forest-low: #0c0c0d;
    --silver: #dcdcdf;
    --silver-dim: #a3a3a8;
    --silver-shine: #f4f4f6;
    --burgundy: #4c1b1e;
    --burgundy-deep: #381214;
    --gold: #d6ad5c;
    --gold-dim: #a8843f;
  }
  * { margin: 0; padding: 0; box-sizing: border-box; }
  html, body {
    width: 1200px;
    height: 900px;
    overflow: hidden;
    background: var(--backdrop);
  }
  .canvas {
    width: 1200px;
    height: 900px;
    display: flex;
    align-items: center;
    justify-content: center;
  }
  .wine-label {
    width: 680px;
    height: 760px;
    background: linear-gradient(180deg, var(--label-black-soft) 0%, var(--label-black) 100%);
    display: flex;
    flex-direction: column;
    box-shadow: 0 20px 60px rgba(0, 0, 0, 0.45);
  }
  .tree-line {
    height: 330px;
    margin: 20px 16px 0;
    border-radius: 2px;
    background:
      radial-gradient(ellipse 60% 45% at 30% 35%, rgba(120, 120, 128, 0.35), transparent 70%),
      radial-gradient(ellipse 50% 40% at 75% 45%, rgba(110, 110, 118, 0.3), transparent 70%),
      linear-gradient(180deg, var(--forest-high) 0%, var(--forest-mid) 45%, var(--forest-low) 85%, var(--label-black) 100%);
  }
  .brand {
    text-align: center;
    margin-top: 34px;
  }
  .brand-name {
    font-family: "Cinzel", serif;
    font-weight: 400;
    font-size: 44px;
    line-height: 1.1;
    letter-spacing: 0.06em;
    color: var(--silver);
  }
  .region {
    font-family: "Cormorant Garamond", serif;
    font-weight: 600;
    font-size: 26px;
    letter-spacing: 0.12em;
    color: var(--silver-dim);
    text-align: center;
    margin-top: 26px;
  }
  .silver-rule {
    height: 14px;
    margin-top: 30px;
    background: linear-gradient(90deg, var(--silver-dim) 0%, var(--silver-shine) 20%, #6c6c70 40%, var(--silver-shine) 60%, #8a8a8e 80%, var(--silver-dim) 100%);
  }
  .varietal-band {
    flex: 1;
    background: linear-gradient(180deg, var(--burgundy) 0%, var(--burgundy-deep) 100%);
    display: flex;
    flex-direction: column;
    align-items: center;
    justify-content: center;
    padding: 0 36px;
  }
  .gold-rule {
    width: 100%;
    height: 1px;
    background: var(--gold-dim);
  }
  .varietal {
    font-family: "Cinzel", serif;
    font-weight: 500;
    font-size: 52px;
    letter-spacing: 0.1em;
    color: var(--gold);
    margin: 24px 0 14px;
  }
  .vintage-line {
    display: flex;
    align-items: center;
    width: 100%;
    gap: 18px;
  }
  .vintage-line .gold-rule { flex: 1; }
  .vintage {
    font-family: "Cormorant Garamond", serif;
    font-weight: 600;
    font-size: 18px;
    letter-spacing: 0.22em;
    color: var(--silver);
    white-space: nowrap;
  }
</style>
</head>
<body>
  <main class="canvas">
    <article class="wine-label">
      <div class="tree-line" role="img" aria-label="Illustrated silhouette of a dark evergreen tree line across the top of the label"></div>
      <header class="brand">
        <h1 class="brand-name">Harrowgate Vineyards</h1>
      </header>
      <p class="region">Willamette Valley</p>
      <div class="silver-rule"></div>
      <section class="varietal-band" aria-label="Burgundy varietal band">
        <div class="gold-rule"></div>
        <h2 class="varietal">SYRAH</h2>
        <div class="vintage-line">
          <span class="gold-rule"></span>
          <span class="vintage">ESTATE | 2023 | GROWN</span>
          <span class="gold-rule"></span>
        </div>
      </section>
    </article>
  </main>
</body>
</html>
```